Business cards need a revamp and change of address. I have included files of current card which has been used for 5 years. Also a photo of my new store fitout which uses a lot of colour and features inspired by cusco Peru. I would like to see design options with and without the butterfly although I do use the butterfly on my current street signage.

Reason: would like to see more designers submit

Target Market(s)

women 35 - 65

Industry/Entity Type

Business

Contact Information for Business Card

Tawra Andean Silver Jewellery & Giftware

Requirements
Must have
• logo frontside
• backside the following text:
• Tawra Jewellery is hand made using the highest quality 950 Peruvian Silver which is purer than 925 Sterling Silver. Tawra's range of unique, handcrafted products are directly sourced from fair trade producer co-operatives, individual artisans and artisan groups from Peru, South America.
• Phone 02 63172846
• 7/118 Marlow Lane Kelby NSW 2861
• Email : sales@tawra-example.com.au
Nice to have
• Like us on face book

```html
<!DOCTYPE html>
<html lang="en">
<head>
<meta charset="utf-8">
<title>Tawra Business Cards</title>
<link rel="stylesheet" href="https://fonts.googleapis.com/css2?family=Cormorant+Garamond:wght@500;700&display=swap">
<style>
  :root {
    --backdrop: #c4c4c4;
    --navy: #434a76;
    --navy-mid: #4f5684;
    --navy-soft: #5d6491;
    --lilac: #7a7fa8;
    --lilac-pale: #868bb2;
    --ink-light: #f2f2f6;
    --wing-blue: #1f8fe0;
    --wing-dark: #173a66;
  }
  * { box-sizing: border-box; margin: 0; padding: 0; }
  html, body { width: 1200px; height: 933px; overflow: hidden; }
  body {
    background: var(--backdrop);
    font-family: "Cormorant Garamond", Georgia, serif;
    color: var(--ink-light);
    position: relative;
  }
  .card {
    position: absolute;
    width: 540px;
    height: 310px;
    overflow: hidden;
    box-shadow: 4px 6px 14px rgba(0,0,0,0.35);
  }
  .card-back {
    left: 620px; top: 40px;
    background: linear-gradient(to bottom,
      var(--navy) 0 13%,
      var(--navy-soft) 13% 16%,
      var(--navy) 16% 28%,
      var(--navy-mid) 28% 34%,
      var(--lilac) 34% 39%,
      var(--navy-soft) 39% 74%,
      var(--navy-mid) 74% 82%,
      var(--navy) 82% 100%);
  }
  .card-front {
    background: linear-gradient(to bottom,
      var(--navy) 0 11%,
      var(--navy-soft) 11% 13%,
      var(--navy) 13% 19%,
      var(--navy-soft) 19% 27%,
      var(--lilac-pale) 27% 62%,
      var(--navy-mid) 62% 72%,
      var(--navy) 72% 85%,
      var(--navy-soft) 85% 87%,
      var(--navy) 87% 100%);
  }
  .card-front.plain { left: 40px; top: 320px; }
  .card-front.with-wing { left: 620px; top: 590px; }

  .contact-row {
    position: absolute;
    top: 62px; left: 0; right: 0;
    display: flex;
    justify-content: space-between;
    padding: 0 34px;
    font-size: 11.5px;
    font-weight: 500;
    letter-spacing: 0.2px;
  }
  .about {
    position: absolute;
    top: 128px; left: 40px; right: 40px;
    text-align: center;
    font-size: 15px;
    font-weight: 500;
    line-height: 1.22;
    letter-spacing: 0.3px;
  }
  .social-note {
    position: absolute;
    top: 240px; left: 0; right: 0;
    text-align: center;
    font-size: 12.5px;
    font-weight: 500;
  }

  .brand-name {
    position: absolute;
    left: 0; right: 0;
    top: 104px;
    text-align: center;
    font-size: 78px;
    font-weight: 700;
    line-height: 1;
    letter-spacing: 1px;
    color: var(--ink-light);
  }
  .butterfly {
    position: absolute;
    left: 150px; top: 112px;
    width: 70px; height: 62px;
    background: radial-gradient(ellipse at 45% 45%, var(--wing-blue) 0 45%, var(--wing-dark) 80%);
    border-radius: 50% 50% 40% 40%;
  }
  .card-front.with-wing .brand-name { left: 60px; }
</style>
</head>
<body>

  <section class="card card-back" aria-label="Card back">
    <div class="contact-row">
      <span class="contact-phone">Phone: 02 63172846</span>
      <span class="contact-address">7/118 Marlow Lane Kelby NSW 2861</span>
      <span class="contact-email">Email: sales@tawra-example.com.au</span>
    </div>
    <p class="about">Tawra Jewellery is hand made using the highest quality 950 Peruvian Silver which is purer than 925 Sterling Silver. Tawra's range of unique, handcrafted products are directly sourced from fair trade producer co-operatives, individual artisans and artisan groups from Peru, South America.</p>
    <p class="social-note">Like us on Folkpage!</p>
  </section>

  <section class="card card-front plain" aria-label="Card front">
    <div class="brand-name">tawra</div>
  </section>

  <section class="card card-front with-wing" aria-label="Card front with butterfly">
    <div class="butterfly" role="img" aria-label="Blue morpho butterfly illustration"></div>
    <div class="brand-name">tawra</div>
  </section>

</body>
</html>
```